Restaurant needs a vertical banner for fried catfish

Our restaurant is looking for an eye-catching 78.75in. x 36in. vertical physical banner ad for our fried catfish. Photos for the fried catfish will be provided as a reference but we will also accept anything similar to the photo. We will be using the following as our receptacle: https://www.plankoria.example/banner-stand/retractable-banner-stands/
The design must incorporate the following flavor texts:
Fried Catfish
Always Fresh!
Made from Scratch
Hand-cut Fillets
The Best Catfish in Texas
Served with fries, hush puppies, and a 32oz fountain drink
Also available by the pound!
The final design should be creative, professional, and eye-catching for customers.
Updates
Colors
Designer to choose colors to be used in the design.
Requirements
Must have
- We are open to any and all design elements, albeit the 'flavor texts' should not overpower, but complement the fried catfish photo. 'Fried Catfish' can be used in lieu of a main title/logo.
Nice to have
- Transparent or textured backgrounds that can encompass any or all part of the banner such as a cutting board, shadows, abstract, etc to show depth are a plus.
- Use of vectors or objects such as ribbons or shapes to encapsulate the 'flavor texts' are also encouraged.

```html
<!DOCTYPE html>
<html lang="en">
<head>
<meta charset="utf-8">
<title>Fried Catfish – Vertical Banner</title>
<link rel="stylesheet" href="https://fonts.googleapis.com/css2?family=Anton&family=Tinos:wght@400;700&family=Open+Sans:wght@400;600;700&family=Oswald:wght@500;600&display=swap">
<style>
  :root {
    --backdrop: #e2e2e2;
    --banner-red: #dd1f26;
    --fresh-green: #3cae49;
    --ink: #111111;
    --paper: #ffffff;
    --photo-warm: #a8652a;
    --photo-light: #e9c98a;
  }
  * { margin: 0; padding: 0; box-sizing: border-box; }
  html, body {
    width: 1200px; height: 817px; overflow: hidden;
    background: var(--backdrop);
  }
  .banner {
    position: absolute; left: 420px; top: 14px;
    width: 360px; height: 788px;
    background: var(--paper);
    overflow: hidden;
    box-shadow: 0 6px 18px rgba(0,0,0,0.18);
  }
  .banner > * { position: absolute; left: 0; width: 100%; }

  .top-band { top: 0; height: 113px; background: var(--banner-red); }
  .top-band::after {
    content: ""; position: absolute; left: 148px; right: 0; bottom: 0;
    height: 3px; background: var(--paper);
  }
  .fresh-tag {
    top: 73px; width: 148px; height: 40px; left: 0;
    background: var(--fresh-green);
    border-radius: 0 4px 0 0;
    color: var(--paper);
    font: 22px/40px "Anton", Impact, sans-serif;
    text-align: center; letter-spacing: 0.2px;
    white-space: nowrap;
  }
  .hero-photo {
    top: 113px; height: 161px;
    background:
      radial-gradient(ellipse 60% 55% at 50% 62%, var(--photo-light) 0%, var(--photo-warm) 55%, transparent 80%),
      linear-gradient(180deg, #b4442d 0%, #8f6a3c 45%, #d8cbb8 100%);
  }
  .hero-rule {
    top: 274px; height: 11px; background: var(--banner-red);
    border-bottom: 2px solid var(--ink);
  }

  .title-block { top: 285px; height: 118px; text-align: center; }
  .title {
    margin-top: 20px;
    font: 400 42px/1 "Tinos", "Times New Roman", serif;
    color: var(--ink);
  }
  .tagline {
    margin-top: 14px;
    font: 700 19px/1 "Tinos", "Times New Roman", serif;
    color: var(--banner-red); letter-spacing: 0.4px;
    white-space: nowrap;
  }

  .sides-band { top: 403px; height: 82px; background: var(--banner-red); }
  .sides-heading {
    top: 408px; text-align: center;
    font: 600 10px/1 "Open Sans", sans-serif; color: var(--paper);
  }
  .side-item {
    top: 424px; width: 90px; text-align: center;
  }
  .side-item.fries { left: 12px; }
  .side-item.hushpuppies { left: 135px; }
  .side-item.drink { left: 258px; }
  .side-photo {
    width: 62px; height: 62px; margin: 0 auto;
    border-radius: 50%; border: 2px solid var(--paper);
  }
  .fries .side-photo { background: radial-gradient(circle at 50% 45%, #ffd54a, #e39a1c 70%, #7a3a12); }
  .hushpuppies .side-photo { background: radial-gradient(circle at 50% 50%, #8a4a22, #5a2a12 60%, #d9d9d9 90%); }
  .drink .side-photo { background: radial-gradient(circle at 50% 50%, #ffffff 40%, #f2d4d4 80%, #ffffff); }
  .side-label {
    margin-top: 10px;
    font: 400 8px/1 "Tinos", serif; color: var(--banner-red);
    letter-spacing: 0.5px; text-transform: uppercase;
    white-space: nowrap;
  }

  .accent-bar {
    left: 18px; width: 324px; height: 23px;
    background: var(--banner-red); border-radius: 4px;
  }
  .accent-bar.upper { top: 505px; }
  .accent-bar.lower { top: 608px; height: 26px; }

  .promises {
    top: 541px; text-align: center;
    font: 400 12px/1.55 "Open Sans", sans-serif; color: var(--banner-red);
  }

  .contact { top: 640px; height: 32px; }
  .social {
    position: absolute; left: 6px; top: 4px;
    font: 600 8px/1 "Open Sans", sans-serif; color: var(--ink);
  }
  .social-row { display: flex; align-items: center; gap: 6px; margin-bottom: 5px; }
  .social-dot {
    width: 10px; height: 10px; border-radius: 50%; background: var(--banner-red);
  }
  .phone-block { position: absolute; right: 4px; top: 0; text-align: right; white-space: nowrap; }
  .phone {
    font: 500 25px/1 "Oswald", sans-serif; color: var(--banner-red);
    letter-spacing: -0.3px;
  }
  .site { font: 700 7px/1.2 "Open Sans", sans-serif; color: var(--ink); }

  .stripe-black { top: 676px; height: 28px; background: var(--ink); }
  .stripe-red { top: 704px; height: 38px; background: var(--banner-red); }
  .stripe-white { top: 742px; height: 17px; background: var(--paper); }
  .stripe-red.base { top: 759px; height: 29px; }
</style>
</head>
<body>
  <div class="banner">
    <div class="top-band"></div>
    <div class="fresh-tag">Always Fresh</div>
    <div class="hero-photo" role="img" aria-label="Plate of golden fried catfish fillets with fries, hushpuppies, tartar sauce and fresh vegetables"></div>
    <div class="hero-rule"></div>

    <div class="title-block">
      <h1 class="title">Fried Catfish</h1>
      <p class="tagline">The Best Catfish in Texas</p>
    </div>

    <div class="sides-band"></div>
    <div class="sides-heading">Served With</div>
    <div class="side-item fries">
      <div class="side-photo" role="img" aria-label="Bowl of french fries"></div>
      <div class="side-label">Fries</div>
    </div>
    <div class="side-item hushpuppies">
      <div class="side-photo" role="img" aria-label="Plate of hushpuppies"></div>
      <div class="side-label">Hushpuppies</div>
    </div>
    <div class="side-item drink">
      <div class="side-photo" role="img" aria-label="Fountain drink cup with straw"></div>
      <div class="side-label">Colddrink</div>
    </div>

    <div class="accent-bar upper"></div>
    <div class="promises">
      Made from Scratch<br>
      Hand-cut Fillets<br>
      Also available by the pound!
    </div>
    <div class="accent-bar lower"></div>

    <div class="contact">
      <div class="social">
        <div class="social-row"><span class="social-dot"></span>yourcompanyname</div>
        <div class="social-row"><span class="social-dot"></span>yourcompanyname</div>
      </div>
      <div class="phone-block">
        <div class="phone">123 456 7890</div>
        <div class="site">www.YOURCOMPANYNAME.com</div>
      </div>
    </div>

    <div class="stripe-black"></div>
    <div class="stripe-red"></div>
    <div class="stripe-white"></div>
    <div class="stripe-red base"></div>
  </div>
</body>
</html>
```